High end business card design for custom homebuilding company

Looking for a high end business card design that is unique and elegant. Can use embossing, foil printing, laser die cutting, or any high end printing technique or high end paper. Will upload current design so you can see the logo and what we are using currently, but we want something more unique and elegant. I included our logo to help with design.

Target Market(s)

High end custom home buyers of $1.5 million plus homes. Also real estate developers of high end communities.

Industry/Entity Type

Business

Contact Information for Business Card

Double sided. We want something very elegant and expensive looking. We are looking to incorporate a combination of perhaps linen paper or a high end paper, with foil stamping or embossing/debossing to make the card look unique, but still elegant. We tend to use blacks and golds, but are open to any ideas. Looking for creative and unique design.

Colors

Designer to choose colors to be used in the design.

Requirements
Must have
• High end, elegant look. Can use foil, embossing, or high end papers like linen. We want to make the card unique and interesting, but elegant and expensive looking.
Nice to have
• I am including just some cards I saw that looked interesting for one reason or another. I like a clean elegant design and like both the clean white style, and the blacks. So not sure if we want a black design or white. Would like to see both.

```html
<!DOCTYPE html>
<html lang="en">
<head>
<meta charset="utf-8">
<title>Ridgeline Custom Homes – Business Card</title>
<link rel="stylesheet" href="https://fonts.googleapis.com/css2?family=Arimo:wght@400;700&display=swap">
<style>
  :root {
    --backdrop: #d5d9d9;
    --paper: #f5f5f3;
    --ink: #1b1b1b;
    --gold: #b08a2a;
    --gold-edge: #8f6d1c;
    --muted: #2e2e2e;
  }
  * { box-sizing: border-box; margin: 0; padding: 0; }
  html, body {
    width: 1200px; height: 1050px; overflow: hidden;
    background: var(--backdrop);
    font-family: "Arimo", Arial, sans-serif;
    color: var(--ink);
  }
  .canvas {
    width: 1200px; height: 1050px;
    display: flex; flex-direction: column; align-items: center; justify-content: center;
    gap: 56px;
  }
  .card {
    position: relative;
    width: 760px; height: 434px;
    background: var(--paper);
    border-bottom: 5px solid var(--gold-edge);
    box-shadow: 0 10px 24px rgba(0,0,0,0.12);
  }
  .brand {
    display: flex; align-items: center; gap: 14px;
  }
  .brand-dot {
    width: 34px; height: 34px; border-radius: 50%;
    background: var(--gold);
    flex: none;
  }
  .brand-name {
    font-weight: 700;
    color: var(--ink);
    letter-spacing: 0.04em;
    white-space: nowrap;
  }
  /* front */
  .card-front .brand { position: absolute; left: 60px; top: 58px; }
  .card-front .brand-name { font-size: 30px; }
  .person {
    position: absolute; left: 60px; top: 150px;
    font-size: 30px; font-weight: 700; letter-spacing: -0.01em;
  }
  .person .surname { color: var(--gold); }
  .contact-list {
    position: absolute; left: 60px; top: 206px;
    list-style: none;
    font-size: 17px; color: var(--muted);
    line-height: 28px;
  }
  .contact-list li { display: flex; align-items: center; gap: 12px; }
  .contact-list svg { width: 16px; height: 16px; flex: none; }
  .address {
    position: absolute; right: 60px; bottom: 48px;
    font-size: 17px; line-height: 24px; text-align: right; color: var(--muted);
  }
  /* back */
  .card-back { display: flex; align-items: center; justify-content: center; }
  .card-back .brand-dot { width: 46px; height: 46px; }
  .card-back .brand-name { font-size: 40px; }
</style>
</head>
<body>
<main class="canvas">

  <section class="card card-front" aria-label="Card front">
    <div class="brand">
      <span class="brand-dot"></span>
      <span class="brand-name">Ridgeline Custom Homes</span>
    </div>

    <p class="person">Avery <span class="surname">Lane</span></p>

    <ul class="contact-list">
      <li>
        <svg viewBox="0 0 16 16" aria-hidden="true"><path d="M4 1.5c-1 .5-2 1.5-2 3 0 4.5 5 10 9.5 10 1.5 0 2.5-1 3-2l-2.8-2-1.6 1.2C8 10.8 5.2 8 4.3 6.4L5.5 4.8z" fill="var(--gold)"/></svg>
        555 014 2291
      </li>
      <li>
        <svg viewBox="0 0 16 16" aria-hidden="true"><rect x="4" y="1" width="8" height="14" rx="1.5" fill="none" stroke="var(--gold)" stroke-width="1.6"/><circle cx="8" cy="12.5" r="0.9" fill="var(--gold)"/></svg>
        555 014 2292
      </li>
      <li>
        <svg viewBox="0 0 16 16" aria-hidden="true"><rect x="1" y="3" width="14" height="10" fill="var(--gold)"/><path d="M1 3l7 6 7-6" fill="none" stroke="var(--paper)" stroke-width="1.2"/></svg>
        info@ridgelinecustomhomes.com
      </li>
      <li>
        <svg viewBox="0 0 16 16" aria-hidden="true"><circle cx="8" cy="8" r="6.5" fill="none" stroke="var(--gold)" stroke-width="1.5"/><path d="M1.5 8h13M8 1.5c-3 3.5-3 9.5 0 13M8 1.5c3 3.5 3 9.5 0 13" fill="none" stroke="var(--gold)" stroke-width="1.1"/></svg>
        www.ridgelinecustomhomes.com
      </li>
    </ul>

    <p class="address">Level 2, 17 Harbour Lane<br>Eastport, VIC 3100</p>
  </section>

  <section class="card card-back" aria-label="Card back">
    <div class="brand">
      <span class="brand-dot"></span>
      <span class="brand-name">Ridgeline Custom Homes</span>
    </div>
  </section>

</main>
</body>
</html>
```